Webdesign für Importeur von Tierbedarfsartikeln
Zielgruppe
Wir importieren Tierbedarfsartikel und verkaufen sie ausschließlich online. Zielgruppe sind in erster Linie Katzenhalter.
Aufgabenstellung
Es gibt eine bestehende Webseite www.pfotenhain24.de Sie wurde bei Webrono erstellt und ist aktiv. Die Seite soll eine professionelle Ansicht erhalten. Schön wären edle Farben, nicht kunterbunt. Wichtig in dem Zusammenhang ist eben, dass sich derjenige mit dem Webronokonzept auskennt.
Dieser Auftrag wird Folgeaufträge erhalten, sprich Logo, Werbeflyer usw. Bilder der Produkte sind vorhanden.

```html
<!DOCTYPE html>
<html lang="de">
<head>
<meta charset="utf-8">
<title>Pfotenhain24 – Startseite</title>
<link href="https://fonts.googleapis.com/css2?family=Lato:wght@300;400;700;900&display=swap" rel="stylesheet">
<style>
:root{
  --navy:#131766;
  --navy-deep:#14185c;
  --blue:#2233f5;
  --blue-text:#1d2ef0;
  --ink:#1a1a1a;
  --muted:#444;
  --grey-card:#f2f2f3;
  --line:#e2e2e2;
  --red:#e03b3b;
  --amber:#f2b900;
}
*{box-sizing:border-box;margin:0;padding:0}
html,body{width:1200px;height:2648px;overflow:hidden}
body{position:relative;font-family:'Lato',sans-serif;color:var(--ink);background:#fff}
.abs{position:absolute}

/* header */
.header{left:0;top:0;width:1200px;height:532px;background:var(--navy)}
.logo{left:150px;top:52px;display:flex;align-items:center;gap:8px;color:#fff;font-size:28px;font-weight:700}
.logo-mark{width:16px;height:16px;background:var(--blue)}
.topinfo{top:22px;font-size:10px;color:#fff;display:flex;align-items:center;gap:6px}
.topinfo svg{width:14px;height:12px}
.search{left:575px;top:52px;width:368px;height:35px;background:#fff;border-radius:2px;font-size:9px;color:#888;padding:12px 14px}
.search svg{position:absolute;right:12px;top:11px;width:12px;height:12px}
.icon{top:60px;width:22px;height:22px}
.cart-count{left:1038px;top:56px;color:#fff;font-size:9px}
.nav{left:150px;top:107px;width:900px;height:46px;background:#fff;display:flex;justify-content:space-around;align-items:center;font-size:11.5px;font-weight:700;color:var(--navy)}

.hero{left:150px;top:153px;width:900px;height:323px;background:var(--blue)}
.hero-sub{left:48px;top:70px;color:#aeb6ff;font-size:21px;font-weight:300}
.hero-title{left:46px;top:100px;color:#fff;font-size:35px;font-weight:900;line-height:35px;letter-spacing:-.3px}
.hero-btn{left:49px;top:203px;width:185px;height:44px;background:#fff;color:var(--navy);font-size:13px;font-weight:700;display:flex;align-items:center;justify-content:center;gap:12px}
.hero-photo{width:220px;height:140px}

/* features */
.feature{top:555px;width:286px;height:126px;background:var(--grey-card);border:1px solid #e6e6e6}
.feature-num{left:18px;top:24px;font-size:38px;font-weight:300;color:#9a9a9a}
.feature-name{left:18px;top:70px;font-size:21px;font-weight:700;color:var(--blue-text)}
.feature-sub{left:18px;top:94px;font-size:15px;color:var(--blue-text)}
.feature-img{right:16px;top:10px;width:124px;height:104px;border-radius:8px}

h2.section-title{position:absolute;left:0;width:1200px;text-align:center;font-size:24px;font-weight:700;color:var(--blue-text)}

.quote{left:128px;top:817px;width:440px;height:120px;border-left:3px solid var(--blue);padding-left:24px;font-size:25.5px;line-height:30px;color:var(--ink)}
.intro{left:619px;top:815px;width:420px;font-size:12.5px;line-height:22.5px;color:#333}
.rule{left:0;top:983px;width:1200px;height:1px;background:var(--line)}

.product-img{height:175px}
.cat-btn{height:36px;border:2px solid #555;border-radius:3px;font-size:12.5px;color:#333;display:flex;align-items:center;justify-content:center;background:#fff}

.slide{top:1795px;height:308px}
.arrow{top:1917px;width:44px;height:44px;border-radius:50%;background:var(--blue);display:flex;align-items:center;justify-content:center}

.sale-card{top:2214px;height:254px;border:1px solid var(--line);background:#fff}
.sale-img{position:absolute;border-radius:6px}
.sale-name{position:absolute;font-size:15.5px;font-weight:700;color:var(--blue-text);line-height:18px;width:165px}
.sale-bar{position:absolute;width:48px;height:2px;background:#333}
.sale-price{position:absolute;font-size:19px;color:var(--red)}
.sale-price s{color:#777;margin-left:8px}
.stock{position:absolute;font-size:15px;color:#333;line-height:18px;padding-left:18px}
.stock::before{content:"";position:absolute;left:0;top:6px;width:7px;height:7px;border-radius:50%;background:var(--amber)}

.footer-links{left:0;top:2538px;width:1200px;height:43px;background:var(--blue);display:flex;justify-content:space-around;align-items:center;padding:0 130px;font-size:11.5px;color:#fff}
.footer-bottom{left:0;top:2581px;width:1200px;height:67px;background:var(--navy-deep);display:flex;justify-content:center;align-items:center;gap:22px}
.pay{height:16px;border-radius:3px;background:#2a3296}
</style>
</head>
<body>

<header class="abs header">
  <div class="abs logo"><span class="logo-mark"></span>Pfotenhain24</div>

  <div class="abs topinfo" style="left:575px">
    <svg viewBox="0 0 14 12"><rect x="1" y="2" width="12" height="8" fill="none" stroke="#fff" stroke-width="1.4"/><circle cx="7" cy="6" r="2" fill="#fff"/></svg>
    Gutscheincode "Plüsch" und 15% auf alle Kuschelbetten sichern
  </div>
  <div class="abs topinfo" style="left:899px">
    <svg viewBox="0 0 14 12"><path d="M7 1 12 3.5V9L7 11.5 2 9V3.5Z" fill="none" stroke="#fff" stroke-width="1.3"/></svg>
    Kostenloser Versand ab €65,00
  </div>

  <div class="abs search">Suche..
    <svg viewBox="0 0 12 12"><circle cx="5" cy="5" r="3.6" fill="none" stroke="#888" stroke-width="1.2"/><path d="M7.6 7.6 11 11" stroke="#888" stroke-width="1.2"/></svg>
  </div>
  <svg class="abs icon" style="left:978px" viewBox="0 0 22 22"><circle cx="11" cy="11" r="9" fill="none" stroke="#fff" stroke-width="1.8"/><circle cx="11" cy="9" r="3" fill="#fff"/><path d="M5.5 17c1.5-3 9.5-3 11 0" fill="#fff"/></svg>
  <svg class="abs icon" style="left:1017px" viewBox="0 0 22 22"><path d="M1 4h3l2.5 10h11L20 7H6" fill="none" stroke="#fff" stroke-width="1.8"/><circle cx="8" cy="18" r="1.6" fill="#fff"/><circle cx="16" cy="18" r="1.6" fill="#fff"/></svg>
  <span class="abs cart-count">(0)</span>

  <nav class="abs nav">
    <span>PFOTENHAIN24</span><span>KATZENKRATZARTIKEL</span><span>PLÜSCHBETTEN</span><span>KATZENSPIELZEUG</span><span>INTERAKTIVE SPIELZEUGE</span><span>ZUBEHÖR</span><span>SALE</span><span>KONTAKT</span>
  </nav>

  <section class="abs hero">
    <p class="abs hero-sub">Pfotenhain24.de</p>
    <h1 class="abs hero-title">GEWINNE TOLLE<br>PREISE GEWINNSPIEL</h1>
    <a class="abs hero-btn">
      <svg width="20" height="16" viewBox="0 0 22 18"><path d="M1 2h3l2.5 9h11L20 5H6" fill="none" stroke="#2233f5" stroke-width="1.8"/><circle cx="8" cy="15" r="1.5" fill="#2233f5"/><circle cx="16" cy="15" r="1.5" fill="#2233f5"/></svg>
      Jetzt einkaufen
    </a>
    <div class="abs hero-photo" role="img" aria-label="Foto: Kätzchen liegt auf weißem Grund" style="left:435px;top:17px;background:linear-gradient(135deg,#eef0f3,#9b948a 55%,#dfe6f0)"></div>
    <div class="abs hero-photo" role="img" aria-label="Foto: Katze spielt am Kratzbaum" style="left:662px;top:17px;background:linear-gradient(135deg,#d4d2cc,#8e8a80 50%,#c9b79a)"></div>
    <div class="abs hero-photo" role="img" aria-label="Foto: Kätzchen im Weidenkorb" style="left:435px;top:164px;background:linear-gradient(180deg,#f5f5f5 40%,#a57b4a)"></div>
    <div class="abs hero-photo" role="img" aria-label="Foto: Katze spielt mit Feder" style="left:662px;top:164px;background:linear-gradient(135deg,#c89a66,#e9ddc9 60%,#f3f0ea)"></div>
  </section>
</header>

<a class="abs feature" style="left:151px">
  <span class="abs feature-num">01</span><span class="abs feature-name">Kratzlounge</span>
  <div class="abs feature-img" role="img" aria-label="Foto: Katzen auf einer Kratzlounge" style="background:linear-gradient(180deg,#f0ece6,#8a6a55)"></div>
</a>
<a class="abs feature" style="left:457px">
  <span class="abs feature-num">02</span><span class="abs feature-name" style="top:66px">Pluschbett</span><span class="abs feature-sub">(Wunschfarbe)</span>
  <div class="abs feature-img" role="img" aria-label="Foto: graues rundes Plüschbett" style="background:radial-gradient(ellipse,#7d8e99,#5a6f80 60%,#f2f2f3 72%)"></div>
</a>
<a class="abs feature" style="left:764px">
  <span class="abs feature-num">03</span><span class="abs feature-name">Spielschlange</span>
  <div class="abs feature-img" role="img" aria-label="Foto: rote Spielschlange" style="background:linear-gradient(135deg,#f2f2f3 30%,#e2463c 50%,#f2f2f3 70%)"></div>
</a>

<h2 class="section-title" style="top:752px">Willkommen bei Pfotenhain24.de</h2>
<p class="abs quote">Hier findest Du eine liebevoll zusammengestellte Auswahl an Zubehör für deine vierbeinigen Familienmitglieder.</p>
<div class="abs intro">
  <p>Unsere Artikel wurden durch unser qualifiziertes, flauschiges Fachpersonal auf Haltbarkeit und Spielspaß geprüft und sind mit schnurrigen Grüßen zu empfehlen!</p>
  <p style="margin-top:22px">Schön, dass du da bist!</p>
</div>
<div class="abs rule"></div>

<h2 class="section-title" style="top:1059px">Unsere Produkte</h2>
<div class="abs product-img" role="img" aria-label="Produktfoto: Kratzsofa mit Katze" style="left:160px;top:1125px;width:255px;background:linear-gradient(180deg,#fff 10%,#2f6b7a 45%,#b8703a 80%,#fff)"></div>
<a class="abs cat-btn" style="left:198px;top:1323px;width:176px">KATZENKRATZARTIKEL</a>
<div class="abs product-img" role="img" aria-label="Produktfoto: rosa Plüschbett" style="left:500px;top:1125px;width:200px;background:radial-gradient(circle,#fbe9ee,#f3c8d4 55%,#fff 70%)"></div>
<a class="abs cat-btn" style="left:508px;top:1323px;width:176px">PLÜSCHBETTEN</a>
<div class="abs product-img" role="img" aria-label="Produktfoto: graue Filzhöhle" style="left:795px;top:1125px;width:230px;background:radial-gradient(ellipse,#6d6d70,#4f4f53 55%,#fff 70%)"></div>
<a class="abs cat-btn" style="left:835px;top:1323px;width:176px">KATZENSPIELZEUG</a>

<div class="abs product-img" role="img" aria-label="Produktfoto: rote Spielschlange" style="left:315px;top:1430px;width:260px;height:150px;background:radial-gradient(ellipse,#e84a44,#f6d4d2 55%,#fff 70%)"></div>
<a class="abs cat-btn" style="left:344px;top:1608px;width:206px">INTERAKTIVE SPIELZEUGE</a>
<div class="abs product-img" role="img" aria-label="Produktfoto: Fusselbürste mit Holzgriff" style="left:670px;top:1412px;width:175px;height:188px;background:linear-gradient(180deg,#fff,#e8e8e8 40%,#e3c49a 75%,#fff)"></div>
<a class="abs cat-btn" style="left:668px;top:1608px;width:177px;border-color:#222">ZUBEHÖR</a>

<h2 class="section-title" style="top:1737px">Top-Produkte</h2>
<div class="abs slide" role="img" aria-label="Foto: Katze schläft auf Kratzsofa vor Pflanze" style="left:150px;width:446px;background:linear-gradient(135deg,#1e4438,#2d6b78 40%,#b8773e 70%,#24493d)"></div>
<div class="abs slide" role="img" aria-label="Foto: Spielschlange auf Holzboden" style="left:612px;width:437px;background:linear-gradient(180deg,#f3d9cf 20%,#e8c69a 45%,#d9b07c)"></div>
<a class="abs arrow" style="left:91px"><svg width="14" height="20" viewBox="0 0 14 20"><path d="M10 2 3 10l7 8" fill="none" stroke="#fff" stroke-width="2"/></svg></a>
<a class="abs arrow" style="left:1065px"><svg width="14" height="20" viewBox="0 0 14 20"><path d="M4 2l7 8-7 8" fill="none" stroke="#fff" stroke-width="2"/></svg></a>

<h2 class="section-title" style="top:2156px">Sale</h2>
<article class="abs sale-card" style="left:150px;width:445px">
  <div class="sale-img" role="img" aria-label="Produktfoto: Kratzsofa aus Pappe" style="left:25px;top:28px;width:220px;height:115px;background:linear-gradient(180deg,#8c7c6c,#6e5f52)"></div>
  <p class="sale-name" style="left:266px;top:45px">Kratzsofa Deluxe L 600 x B 280 x H230mm mit leichten Dellen</p>
  <span class="sale-bar" style="left:266px;top:105px"></span>
  <p class="sale-price" style="left:269px;top:124px">19,99 € <s>25,99 €</s></p>
  <p class="stock" style="left:269px;top:170px">Nur noch wenige<br>vorrätig</p>
</article>
<article class="abs sale-card" style="left:612px;width:437px">
  <div class="sale-img" role="img" aria-label="Produktfoto: Kratzball auf Holzgestell" style="left:45px;top:12px;width:170px;height:225px;background:linear-gradient(180deg,#c3a77e 45%,#6a4a38)"></div>
  <p class="sale-name" style="left:256px;top:37px">Kratzball mit leichten optischen Mängeln</p>
  <span class="sale-bar" style="left:256px;top:90px"></span>
  <p class="sale-price" style="left:259px;top:109px">19,99 € <s>25,99 €</s></p>
  <p class="stock" style="left:259px;top:155px">Nur noch wenige<br>vorrätig</p>
</article>

<footer>
  <nav class="abs footer-links">
    <span>Impressum</span><span>Datenschutzerklärung</span><span>Cookie-Richtlinie</span><span>Zahlung &amp; Versand</span><span>Allgemeine Geschäftsbedingungen</span><span>Widerrufsrecht</span>
  </nav>
  <div class="abs footer-bottom">
    <span class="pay" style="width:74px"></span>
    <span class="pay" style="width:22px"></span>
    <span class="pay" style="width:22px;border-radius:50%"></span>
    <span class="pay" style="width:48px"></span>
    <span class="pay" style="width:60px"></span>
    <span class="pay" style="width:26px"></span>
    <span class="pay" style="width:26px;border-radius:8px"></span>
  </div>
</footer>

</body>
</html>
```